Wine Labels for new product to attract Millenial consumers

SipLark Design Brief
1. Intro:
Marrabel Cellars is a 120 year old family owned Australian wine company renowned for producing traditional premium quality wines. This project is aimed at breaking through this perception of Marrabel to show main stream Australian retailers that we can be innovative and relevant and that we know who their millennial shoppers are and we know how to attract their attention. This needs to be achieved through the combination of innovative and clever design paired with a product that challenges conventional Australian wine philosophies and appeals to those wine drinkers seeking authentic and alternative wine experiences.
2. Feelings:
This new wine should evoke a new set of feelings in retailers that they don’t usually associate with Marrabel Cellars. Retailers should feel excited, challenged and impressed by our knowledge of the millennial demographic. The packaging should make the shopper feel surprised, curious, cool, aspirational, understood, adventurous, individual, fashionable, progressive and engaged. It also needs to evoke a sense of the occasion it should be consumed in, with food and friends in a fun environment and evoke a sense of conviviality and a desire for shared social interaction.
3. Look + Feel:
It shouldn’t look or feel like anything Marrabel Cellars is known for and has done before. It should not carry our branding or logo, this should be a standalone product range. It should feel modern, cool, clever and hip. It should feel real, authentic, artisanal and most of all it should challenge the traditional visual discourse of wine as bored, tired, stiff and conservative. The design should be respected piece of art in its own right. It should make the shopper feel like getting a few friends around for dinner and drinks.
4. Brand Position:
This product range needs to challenge the existing brand positioning of Marrabel Cellars. It should clearly target the millennial demographic and the hipster sub culture who are being lured into new alcohol categories by cool design and positioning. “Exposed to a barrage of drinks offerings, the report found that wine is in danger of losing Generation Y to other more engaging drinks categories such as beer, cider and spirits ……. With 18-25 year olds accounting for 25% of the wine drinking population, Millennials represent an important sector of the wine market, thus keeping their attention and interest should remain a priority for wine brands.” Cork Insight Report. “…. Wine is becoming increasingly cool with the influencers and trend setters of a whole new generation.” Pour Weekly.
5. Needs:
2 wine labels, one white and one red, but linked by design. Should fit a 500 ml glass bottle and design should be able to carry over to some innovative packaging into small lots of 4 or 6 like beer. For the purpose of design use the name SipLark White and SipLark Red. Relating the wine to food and how it should be consumed is important as this needs to be seen as a lifestyle accessory to food to combat the anti-alcohol lobby and the socially acceptable practise of eating and drinking together as part of a social experience. An area for approximately 200 words of mandatory information and declarations needs to be provided.

https://www.pinboardia.example/MarrabelCellars/siplark-moodboard/

Target Market(s)

Industry/Entity Type

Font styles to use
Sans Serif

Requirements
Must have
• Full brief in project description
Nice to have
Should not have

```html
<!DOCTYPE html>
<html lang="en">
<head>
<meta charset="utf-8">
<title>SipLark White 2014 — Label</title>
<link rel="stylesheet" href="https://fonts.googleapis.com/css2?family=Crimson+Pro:wght@400&family=Montserrat:wght@600&display=swap">
<style>
  :root {
    --paper: #ffffff;
    --label-paper: #f4f1ec;
    --label-orange: #d5562b;
    --label-orange-light: #e0703f;
    --ghost-text: rgba(240, 150, 110, 0.45);
    --accent: #e0522a;
    --title-white: #fbf6f1;
  }
  html, body {
    margin: 0;
    width: 1200px;
    height: 917px;
    overflow: hidden;
    background: var(--paper);
  }
  .canvas {
    position: relative;
    width: 1200px;
    height: 917px;
  }
  .label {
    position: absolute;
    left: 435px;
    top: 58px;
    width: 330px;
    height: 800px;
    background: var(--label-orange);
    overflow: hidden;
  }
  .label-header {
    position: absolute;
    left: 0; top: 0;
    width: 100%;
    height: 150px;
    background: var(--label-paper);
  }
  .varietal-vintage {
    position: absolute;
    left: 0; right: 0; top: 34px;
    display: flex;
    justify-content: center;
    align-items: center;
    gap: 14px;
    font-family: "Montserrat", sans-serif;
    font-weight: 600;
    color: var(--accent);
  }
  .varietal {
    font-size: 34px;
    letter-spacing: 1px;
    margin-top: 18px;
  }
  .divider {
    width: 2px;
    height: 84px;
    background: var(--accent);
  }
  .vintage {
    display: grid;
    grid-template-columns: repeat(2, 26px);
    font-size: 38px;
    line-height: 42px;
    text-align: center;
  }
  .label-body {
    position: absolute;
    left: 0; top: 150px;
    width: 100%;
    height: 650px;
    background: linear-gradient(160deg, var(--label-orange-light), var(--label-orange) 60%);
  }
  .torn-edge {
    position: absolute;
    left: 0; top: 140px;
    width: 330px;
    height: 60px;
  }
  .wordmark, .wordmark-ghost {
    position: absolute;
    margin: 0;
    font-family: "Crimson Pro", serif;
    font-weight: 400;
    writing-mode: vertical-rl;
    transform: rotate(180deg);
    white-space: nowrap;
    line-height: 1;
  }
  .wordmark {
    left: 112px;
    bottom: 70px;
    font-size: 100px;
    color: var(--title-white);
    letter-spacing: 1px;
  }
  .wordmark-ghost {
    color: var(--ghost-text);
  }
  .ghost-left { left: 36px; bottom: 40px; font-size: 66px; }
  .ghost-right-a { left: 220px; bottom: 150px; font-size: 56px; }
  .ghost-right-b { left: 282px; bottom: 40px; font-size: 44px; }
</style>
</head>
<body>
<main class="canvas">
  <section class="label" aria-label="SipLark White 2014 wine label">
    <header class="label-header">
      <div class="varietal-vintage">
        <span class="varietal">WHITE</span>
        <span class="divider"></span>
        <span class="vintage"><span>2</span><span>0</span><span>1</span><span>4</span></span>
      </div>
    </header>
    <div class="label-body">
      <span class="wordmark-ghost ghost-left" aria-hidden="true">sip lark sip lark</span>
      <span class="wordmark-ghost ghost-right-a" aria-hidden="true">sip lark</span>
      <span class="wordmark-ghost ghost-right-b" aria-hidden="true">sip lark</span>
      <h1 class="wordmark">sip lark</h1>
    </div>
    <svg class="torn-edge" viewBox="0 0 330 60" aria-hidden="true">
      <path fill="#f4f1ec" d="M0 0 H330 V26 C318 30 312 22 300 28 C290 34 282 24 270 30 C258 38 250 26 238 34 C226 42 214 28 200 32 C188 36 180 26 168 30 C156 34 146 46 132 40 C120 34 112 40 100 36 C88 30 80 42 66 38 C54 34 44 44 32 40 C20 36 12 44 0 42 Z"/>
    </svg>
  </section>
</main>
</body>
</html>
```